Business Card Design Project

We need a business card to reflect the design of our website - just so it all ties in - it has a retro feel and can be found at http://www.velorasoulpair.com
We will need our phone 0437 215 964
Web address, and email velorapair@fernmail.com included
Our catch cry is "Classic Cocktail Music"
Perfect Live Music for Private & Corporate Events, Weddings and Dinner Music
Our names should be included :-
Maribel Thorne / piano & Dennis Holloway / bass
I am now also including our logo so that it can be included (in part or whole) somehow in the design
My partner thinks we should include our logo in some form in the design of the card - i will attach this here for you. I will attach eps but if you prefer another format please let me know
Regards
Mari

```html
<!DOCTYPE html>
<html lang="en">
<head>
<meta charset="utf-8">
<title>Velora Soul Pair – Business Card</title>
<link rel="stylesheet" href="https://fonts.googleapis.com/css2?family=Josefin+Sans:wght@600;700&display=swap">
<style>
  :root {
    --backdrop: #3b3b3b;
    --card: #8fb4b2;
    --frame: #6b7675;
    --ink: #2a2a2a;
    --badge: #fdf3d2;
  }
  html, body {
    margin: 0;
    padding: 0;
    width: 1200px;
    height: 720px;
    overflow: hidden;
    background: var(--backdrop);
  }
  .card {
    position: absolute;
    left: 40px;
    top: 40px;
    width: 1120px;
    height: 640px;
    background: var(--card);
    font-family: "Josefin Sans", sans-serif;
    color: var(--ink);
  }
  .frame-dashed {
    position: absolute;
    left: 53px; top: 53px;
    width: 1012px; height: 532px;
    border: 1.5px dashed var(--frame);
    box-sizing: border-box;
  }
  .frame-solid {
    position: absolute;
    left: 62px; top: 62px;
    width: 996px; height: 516px;
    border: 2px solid var(--frame);
    box-sizing: border-box;
  }
  .badge {
    position: absolute;
    width: 64px; height: 64px;
    border-radius: 50%;
    background: var(--badge);
    border: 2.5px solid var(--ink);
    box-sizing: border-box;
    display: flex;
    align-items: center;
    justify-content: center;
  }
  .badge svg { display: block; }
  .badge--person { left: 306px; top: 117px; }
  .badge--phone  { left: 394px; top: 290px; }
  .badge--mail   { left: 339px; top: 464px; }
  .names {
    position: absolute;
    left: 398px;
    top: 105px;
    margin: 0;
    font-size: 34px;
    font-weight: 600;
    font-variant: small-caps;
    letter-spacing: 1.5px;
    line-height: 44px;
    white-space: nowrap;
  }
  .names .first { display: block; padding-left: 2px; }
  .names .second { display: block; margin-left: -8px; }
  .phone {
    position: absolute;
    left: 490px;
    top: 300px;
    margin: 0;
    font-size: 33px;
    font-weight: 600;
    letter-spacing: 4px;
    white-space: nowrap;
  }
  .email {
    position: absolute;
    left: 428px;
    top: 482px;
    margin: 0;
    font-size: 29px;
    font-weight: 600;
    font-variant: small-caps;
    letter-spacing: 1px;
    white-space: nowrap;
  }
  .divider {
    position: absolute;
    height: 12px;
  }
  .divider--upper { left: 347px; top: 236px; width: 428px; }
  .divider--lower { left: 353px; top: 409px; width: 428px; }
  .divider .rule {
    position: absolute;
    left: 0; right: 0; top: 5px;
    height: 2px;
    background: var(--ink);
  }
  .divider .flourish {
    position: absolute;
    left: 164px; top: 2px;
    width: 100px; height: 8px;
    border-radius: 4px;
    background: var(--ink);
  }
</style>
</head>
<body>
  <main class="card">
    <div class="frame-dashed"></div>
    <div class="frame-solid"></div>

    <div class="badge badge--person">
      <svg width="30" height="34" viewBox="0 0 30 34" aria-hidden="true">
        <circle cx="15" cy="9" r="8" fill="#2a2a2a"/>
        <path d="M2 34 V26 Q2 18 10 18 H20 Q28 18 28 26 V34 Z" fill="#2a2a2a"/>
      </svg>
    </div>
    <h1 class="names">
      <span class="first">Maribel Thorne / piano</span>
      <span class="second">&amp; Dennis Holloway / bass</span>
    </h1>

    <div class="divider divider--upper">
      <div class="rule"></div>
      <div class="flourish" role="img" aria-label="Small scroll flourish"></div>
    </div>

    <div class="badge badge--phone">
      <svg width="34" height="26" viewBox="0 0 34 26" aria-hidden="true">
        <path d="M2 9 Q17 -2 32 9 L29 13 L23 11 L22 7 Q17 5 12 7 L11 11 L5 13 Z" fill="#2a2a2a"/>
        <path d="M9 12 H25 L30 24 H4 Z" fill="#2a2a2a"/>
        <circle cx="17" cy="18" r="3.5" fill="#fdf3d2"/>
      </svg>
    </div>
    <p class="phone">0437 215 964</p>

    <div class="divider divider--lower">
      <div class="rule"></div>
      <div class="flourish" role="img" aria-label="Small scroll flourish"></div>
    </div>

    <div class="badge badge--mail">
      <svg width="32" height="22" viewBox="0 0 32 22" aria-hidden="true">
        <rect x="1" y="1" width="30" height="20" fill="#2a2a2a"/>
        <path d="M2 2 L16 13 L30 2" fill="none" stroke="#fdf3d2" stroke-width="1.8"/>
      </svg>
    </div>
    <p class="email">velorapair@fernmail.com</p>
  </main>
</body>
</html>
```